TAILWIND FIELDS Pet Resorts Outdoor Signage

4 x 8 outdoor signage design for our two locations

Target Market(s)

Existing and New Customers

Industry/Entity Type

Pet Care

Font styles to use
Sans Serif

Colors

Designer to choose colors to be used in the design.

```html
<!DOCTYPE html>
<html lang="en">
<head>
<meta charset="utf-8">
<title>Tailwind Fields Pet Resorts – Outdoor Sign</title>
<link rel="stylesheet" href="https://fonts.googleapis.com/css2?family=Oswald:wght@500&family=Josefin+Sans:wght@400;700&family=Montserrat:wght@700&display=swap">
<style>
  :root {
    --navy: #17103f;
    --navy-deep: #0e0a2a;
    --orange: #f9ae42;
    --white: #ffffff;
    --backdrop: #e6e6e6;
    --meadow-light: #b9a46a;
    --meadow-dark: #6f8a3c;
  }
  * { margin: 0; padding: 0; box-sizing: border-box; }
  html, body {
    width: 1200px; height: 1200px; overflow: hidden;
    background: var(--backdrop);
  }
  .sign {
    position: absolute; left: 0; top: 300px;
    width: 1200px; height: 600px; overflow: hidden;
    background: var(--orange);
  }
  .sign-shapes { position: absolute; inset: 0; }
  .brand-name {
    position: absolute; left: 373px; top: 150px; width: 300px;
    font-family: "Josefin Sans", sans-serif; font-weight: 700;
    font-size: 58px; line-height: 1.1; color: var(--orange);
    letter-spacing: 1px;
  }
  .contact-box {
    position: absolute; left: 257px; top: 462px;
    width: 371px; height: 93px; border-radius: 12px;
    background: var(--orange);
    padding: 8px 0 0 54px;
    font-family: "Josefin Sans", sans-serif; font-weight: 700;
    color: var(--navy);
  }
  .contact-phone { font-size: 36px; line-height: 40px; }
  .contact-web { font-size: 30px; line-height: 40px; }
  .services {
    position: absolute; left: 694px; top: 132px;
    list-style: none;
    font-family: "Oswald", sans-serif; font-weight: 500;
    font-size: 46px; line-height: 71px; color: var(--orange);
  }
  .services li { display: flex; align-items: center; white-space: nowrap; }
  .services .bullet {
    display: inline-block; width: 14px; height: 14px;
    background: var(--white); margin-right: 14px;
  }
  .services .bullet.inline { margin-left: 22px; }
  .rule {
    position: absolute; left: 651px; top: 420px;
    width: 518px; height: 5px; background: var(--orange);
  }
  .tagline {
    position: absolute; left: 654px; top: 474px;
    display: flex; align-items: center;
    font-family: "Montserrat", sans-serif; font-weight: 700;
    color: var(--white);
  }
  .tagline-resort { font-size: 38px; letter-spacing: 0.5px; }
  .tagline-divider {
    width: 3px; height: 78px; background: var(--white);
    margin: 0 14px 0 10px;
  }
  .tagline-breeds { font-size: 34px; line-height: 32px; }
</style>
</head>
<body>
  <section class="sign">
    <svg class="sign-shapes" width="1200" height="600" viewBox="0 0 1200 600">
      <defs>
        <linearGradient id="meadow" x1="0" y1="0" x2="0" y2="1">
          <stop offset="0" stop-color="#c7c3b6"/>
          <stop offset="0.35" stop-color="var(--meadow-light)"/>
          <stop offset="1" stop-color="var(--meadow-dark)"/>
        </linearGradient>
      </defs>
      <path class="arch-edge" d="M0,140 Q600,-62 1200,140 L1200,600 L0,600 Z" fill="var(--navy-deep)"/>
      <path class="arch-panel" d="M0,160 Q600,-40 1200,180 L1200,600 L0,600 Z" fill="var(--navy)"/>
      <path class="photo-area" role="img" aria-label="Photo of a happy puppy running across a grassy field"
            d="M0,168 Q170,106 331,76 Q380,340 231,600 L0,600 Z" fill="url(#meadow)"/>
    </svg>

    <div class="brand-name">TAILWIND<br>FIELDS</div>

    <div class="contact-box">
      <div class="contact-phone">905-555-0148</div>
      <div class="contact-web">www.tailwindfields.ca</div>
    </div>

    <ul class="services">
      <li><span class="bullet"></span>BOARDING<span class="bullet inline"></span>DAYCARE</li>
      <li><span class="bullet"></span>TRAINING</li>
      <li><span class="bullet"></span>FULL-SERVICE SALON</li>
      <li><span class="bullet"></span>PET TAXI &amp; MORE</li>
    </ul>

    <div class="rule"></div>

    <div class="tagline">
      <span class="tagline-resort">PET RESORT</span>
      <span class="tagline-divider"></span>
      <span class="tagline-breeds">ALL BREED<br>FRIENDLY</span>
    </div>
  </section>
</body>
</html>
```